Graphic Design - Website Header - Leaderboard

Hello,
I am looking for a design to go above the navigation on my website/blog. Design will include an image, name of website and some followup wording or taglines.

Website will be a pagecraft blog about mens lifestyle, but will be more rugged in nature, the anti-VR blog for men. A man's man blog - think Kestwick Rider image. Inspiring young men about women, whiskey, boots, jeans & proper manners .. that sort of thing. Want to appeal to cosmopolitan men .. not actual cowboys, so no cowboy hats.

Would like an image on the left of the face of a tough looking, handsome man, looking into the page, with scruff. Man must be a drawing or abstract image, no photo.

Image should be at least 900 x 200 pixels and use earth tones. Navigation under image will be something like - About, Lifestyle, Attire, Transport, Man Skills, Booze, Women, Contact.

Name of blog will be CedarAndFlint.example
Updates

Serious about a legit design .. cmon people . this is an easy one ...please read my detailed brief.  Let me know if you have questions.... and, THANK YOU !

Reason: still looking for designs .. very detailed specs in the brief Thank You !

Target Market(s)

23-40yr old men, looking for tips on how to look and act like a cool guy and appeal to women

Industry/Entity Type

Graphic Design

Requirements
Must have
• 1. Drawing of a Man with scruff on left side of graphic, looking into the page (to the right). Not a photograph - an image or drawing. See uploaded image - want something ssimilar in style.

2. Masculine Earth Tones & Fonts. textured background

3. Include name of site in middle ..with tagline below it
"Inspiring Men About Women, Whiskey & Proper Manners"
(ability to easily change the tagline)
Nice to have
• Ability to easily use this design on a business card
Should not have
• 1. Actual photo of man
2. Shirtless guy
3. Cowboy hat or cigarette

```html
<!DOCTYPE html>
<html lang="en">
<head>
<meta charset="utf-8">
<title>Cedar &amp; Flint – Header</title>
<link rel="stylesheet" href="https://fonts.googleapis.com/css2?family=PT+Sans:wght@400;700&display=swap">
<style>
  :root {
    --leather-top: #c4875a;
    --leather-mid: #dcaa7b;
    --leather-low: #b77a4c;
    --leather-edge: #7a4324;
    --frame: #5a2e14;
    --title-ink: #3b1c0a;
    --title-glow: #f1c9a0;
    --rule: #4a240e;
    --band: #2b1408;
    --band-text: #fbf3e8;
    --portrait-light: #d6d2cc;
    --portrait-mid: #9d9891;
    --portrait-dark: #3a3632;
  }
  html, body {
    margin: 0;
    padding: 0;
    width: 1200px;
    height: 267px;
    overflow: hidden;
    background: #ffffff;
  }
  .site-header {
    position: relative;
    width: 1200px;
    height: 267px;
    box-sizing: border-box;
    border: 2px solid var(--frame);
    overflow: hidden;
    background:
      radial-gradient(ellipse 55% 70% at 55% 45%, var(--leather-mid) 0%, rgba(220,170,123,0) 70%),
      linear-gradient(180deg, var(--leather-top) 0%, var(--leather-mid) 40%, var(--leather-low) 80%, var(--leather-edge) 100%);
    font-family: "PT Sans", Arial, sans-serif;
  }
  .landscape {
    position: absolute;
    left: 200px;
    right: 0;
    top: 128px;
    height: 100px;
    background: linear-gradient(180deg, rgba(169,104,63,0) 0%, rgba(169,104,63,0.55) 45%, rgba(140,80,45,0.6) 100%);
  }
  .portrait {
    position: absolute;
    left: 0;
    top: 0;
    width: 282px;
    height: 267px;
  }
  .portrait__head {
    position: absolute;
    left: 38px;
    top: 4px;
    width: 118px;
    height: 170px;
    border-radius: 48% 48% 44% 44%;
    background: radial-gradient(ellipse 60% 55% at 55% 45%, var(--portrait-light) 0%, var(--portrait-mid) 60%, var(--portrait-dark) 100%);
  }
  .portrait__body {
    position: absolute;
    left: 0;
    top: 140px;
    width: 282px;
    height: 127px;
    background: radial-gradient(ellipse 60% 70% at 45% 30%, var(--portrait-light) 0%, var(--portrait-mid) 55%, var(--portrait-dark) 100%);
    clip-path: polygon(22% 0, 62% 0, 84% 22%, 96% 60%, 100% 100%, 0 100%, 2% 50%, 12% 18%);
  }
  .title-rule {
    position: absolute;
    left: 234px;
    width: 780px;
    height: 2px;
    background: var(--rule);
    box-shadow: 0 1px 0 rgba(255,225,190,0.45);
  }
  .title-rule--top { top: 43px; }
  .title-rule--bottom { top: 162px; }
  .site-title {
    position: absolute;
    left: 234px;
    width: 780px;
    top: 46px;
    margin: 0;
    text-align: center;
    font-size: 88px;
    font-weight: 700;
    line-height: 112px;
    letter-spacing: 1px;
    color: var(--title-ink);
    text-shadow: 0 2px 0 var(--title-glow);
  }
  .tagline-band {
    position: absolute;
    left: 309px;
    right: 0;
    top: 216px;
    height: 51px;
    background: var(--band);
    display: flex;
    align-items: center;
  }
  .tagline {
    margin: 0 0 0 15px;
    color: var(--band-text);
    font-size: 25px;
    font-weight: 700;
    letter-spacing: 0.3px;
    white-space: nowrap;
  }
</style>
</head>
<body>
  <header class="site-header">
    <div class="landscape" role="img" aria-label="Faint rolling hills across the horizon"></div>
    <div class="portrait" role="img" aria-label="Stylised grayscale drawing of a rugged man with stubble in a collared shirt, looking to the right">
      <div class="portrait__body"></div>
      <div class="portrait__head"></div>
    </div>
    <div class="title-rule title-rule--top"></div>
    <h1 class="site-title">Cedar &amp; Flint</h1>
    <div class="title-rule title-rule--bottom"></div>
    <div class="tagline-band">
      <p class="tagline">Notes for Men on Courtship, Bourbon &amp; Good Conduct.</p>
    </div>
  </header>
</body>
</html>
```